Business Card for a Mortgage Agent (myself)

I need a business card for my new job as Mortgage Agent. The Broker's logo is to be on the card as well as the brokerage License number. Not sure if to include a photo or not. Info to be on card.
Dario Fenn
Mortgage Agent
Lic # M37115908
Cell: 555-714-2093
Email: dariofennk.ma@quillpost.com
Web: www.kenhartwellmortgages.com
TQV Brokerage Lic. # 58219

```html
<!DOCTYPE html>
<html lang="en">
<head>
<meta charset="utf-8">
<title>Dario Fenn – Mortgage Agent Business Card</title>
<link href="https://fonts.googleapis.com/css2?family=Arimo:wght@400;700&display=swap" rel="stylesheet">
<style>
  :root {
    --backdrop: #e4e4e4;
    --card-dark: #2a2a2c;
    --card-deep: #1f1f21;
    --brand-blue: #0b4fa0;
    --brand-yellow: #f5c400;
    --text-light: #f2f2f2;
    --divider: #6a6a6e;
  }
  * { margin: 0; padding: 0; box-sizing: border-box; }
  html, body {
    width: 1200px; height: 801px; overflow: hidden;
    background: var(--backdrop);
    font-family: "Arimo", Arial, sans-serif;
  }
  .sheet { position: relative; width: 1200px; height: 801px; }
  .card {
    position: absolute; top: 246px;
    width: 540px; height: 308px;
    border-radius: 4px; overflow: hidden;
    box-shadow: 0 10px 30px rgba(0,0,0,.22);
  }
  .card--front { left: 40px; background: var(--card-dark); }
  .card--back { left: 620px; background: var(--card-deep); }
  .card__bands { position: absolute; inset: 0; }

  .brand { position: absolute; left: 40px; top: 104px; width: 180px; }
  .brand__mark {
    display: flex; align-items: center; gap: 10px;
    color: var(--brand-yellow); font-weight: 700; font-size: 44px; letter-spacing: 4px;
  }
  .brand__square { width: 22px; height: 22px; background: var(--brand-yellow); }
  .brand__name {
    margin-top: 6px; color: var(--brand-yellow);
    font-weight: 700; font-size: 13px; letter-spacing: .5px;
  }

  .divider {
    position: absolute; left: 238px; top: 52px;
    width: 1px; height: 132px; background: var(--divider);
  }
  .agent { position: absolute; left: 256px; top: 48px; color: var(--text-light); }
  .agent__name { color: var(--brand-blue); font-weight: 700; font-size: 22px; line-height: 1.1; }
  .agent__role, .agent__licence { font-size: 13px; line-height: 1.25; }
  .contacts { margin-top: 12px; list-style: none; }
  .contacts__item {
    display: flex; align-items: center; gap: 7px;
    font-size: 12.5px; line-height: 1.45;
  }
  .contacts__icon { width: 12px; height: 12px; flex: none; }

  .brokerage-licence {
    position: absolute; right: 26px; bottom: 26px;
    color: var(--text-light); font-size: 15px;
  }

  .back__texture {
    position: absolute; inset: 0;
    background: linear-gradient(120deg, #1c1c1e 0%, #2c2c2f 55%, #4a4a4e 100%);
  }
  .back__brand {
    position: absolute; right: 70px; top: 190px;
    display: flex; align-items: center; gap: 8px;
    color: var(--brand-yellow); font-weight: 700; font-size: 24px; letter-spacing: 2px;
  }
  .back__square { width: 12px; height: 12px; background: var(--brand-yellow); }
</style>
</head>
<body>
<main class="sheet">
  <section class="card card--front" aria-label="Business card front">
    <svg class="card__bands" viewBox="0 0 540 308" aria-hidden="true">
      <path d="M0,292 C170,300 300,250 372,168 C420,114 480,92 540,80 L540,308 L0,308 Z" fill="var(--brand-blue)"/>
      <path d="M0,276 C150,284 262,238 322,150 C272,226 160,272 0,284 Z" fill="var(--brand-yellow)"/>
    </svg>

    <div class="brand">
      <div class="brand__mark"><span class="brand__square"></span>TQV</div>
      <div class="brand__name">TRUE QUAY VENTURES</div>
    </div>

    <div class="divider"></div>

    <div class="agent">
      <p class="agent__name">Dario Fenn</p>
      <p class="agent__role">Mortgage Agent</p>
      <p class="agent__licence">Lic # M37115908</p>
      <ul class="contacts">
        <li class="contacts__item">
          <svg class="contacts__icon" viewBox="0 0 12 12"><path d="M2.5 1 L4.5 1 L5.2 3.6 L4 4.6 C4.7 6 6 7.3 7.4 8 L8.4 6.8 L11 7.5 L11 9.5 C11 10.3 10.3 11 9.5 11 C5 11 1 7 1 2.5 C1 1.7 1.7 1 2.5 1 Z" fill="var(--brand-blue)"/></svg>
          555-714-2093
        </li>
        <li class="contacts__item">
          <svg class="contacts__icon" viewBox="0 0 12 12"><rect x="1" y="2.5" width="10" height="7" fill="var(--brand-blue)"/><path d="M1 2.5 L6 6.5 L11 2.5" stroke="var(--card-dark)" stroke-width="1" fill="none"/></svg>
          dariofennk.ma@quillpost.com
        </li>
        <li class="contacts__item">
          <svg class="contacts__icon" viewBox="0 0 12 12"><circle cx="6" cy="6" r="5" fill="var(--brand-blue)"/><path d="M1 6 H11 M6 1 C3.5 4 3.5 8 6 11 M6 1 C8.5 4 8.5 8 6 11" stroke="var(--card-dark)" stroke-width=".8" fill="none"/></svg>
          www.kenhartwellmortgages.com
        </li>
      </ul>
    </div>

    <p class="brokerage-licence">TQV Brokerage Lic. # 58219</p>
  </section>

  <section class="card card--back" aria-label="Business card back">
    <div class="back__texture" role="img" aria-label="Dark embossed tile texture fading from black to grey"></div>
    <div class="back__brand"><span class="back__square"></span>TQV</div>
  </section>
</main>
</body>
</html>
```